Website Refresh Needed - Large Couples Therapy Group

We are a large couples counselling group in Australia, and we have some key pages of our website that need refreshing, as it's a few years old now.
Similar colour palette as currently, and the same colours as the logo. No new logo required.
Total of 7 new (updated) page templates designs are needed:
1. HOME: https://www.velmoraclinic.com.au/
2: CONTACT US: https://www.velmoraclinic.com.au/contact/
3: RC CITY PAGE: https://www.velmoraclinic.com.au/city/sydney/
4: ST CITY PAGE: https://www.velmoraclinic.com.au/our-counselling/sex-therapy/sex-therapy-sydney/
5: ALL BLOGS: https://www.velmoraclinic.com.au/blog/
6: BLOG: https://www.velmoraclinic.com.au/sexual-desires-in-men-and-women-what-are-the-real-differences/
7: MAIN STANDARD PAGE: https://www.velmoraclinic.com.au/our-counselling/couples-relationship-counselling/

Target Market(s)

couples who are going through a crisis in their relationship or marriage.

Number of Pages Required

5+ page

Colors
86cfc6
b8a6cd
cfdfed

Requirements
Must have
• Calm, reassuring colours. People are stressed and need to know we can help.
Should not have
• No bright oranges or yellows.

```html
<!DOCTYPE html>
<html lang="en">
<head>
<meta charset="utf-8">
<title>Velmora Clinic – Expert Relationship &amp; Marriage Counselling</title>
<link href="https://fonts.googleapis.com/css2?family=Poppins:wght@300;400;500&display=swap" rel="stylesheet">
<style>
:root{
  --teal:#148c98;
  --teal-dark:#0f7580;
  --red:#ec1c26;
  --ink:#2b2d33;
  --muted:#7b7f87;
  --line:#e6e8ec;
  --soft:#f3f5f9;
  --footer:#2a2b2f;
  --white:#ffffff;
}
*{box-sizing:border-box;margin:0;padding:0}
html,body{width:1200px;height:4256px;overflow:hidden}
body{font-family:"Poppins",sans-serif;color:var(--ink);background:var(--white);position:relative;font-weight:300}
.abs{position:absolute}
a{color:inherit;text-decoration:none}

/* header */
.site-header{position:absolute;left:0;top:0;width:1200px;height:110px;z-index:3}
.brand{position:absolute;left:102px;top:32px;display:flex;align-items:center;gap:10px}
.brand-dot{width:30px;height:30px;border-radius:50%;background:var(--teal)}
.brand-name{font-size:22px;font-weight:400;color:var(--teal);line-height:1}
.brand-tag{position:absolute;left:142px;top:62px;font-size:9px;color:var(--teal);white-space:nowrap}
.util-nav{position:absolute;right:104px;top:27px;font-size:10px;color:#a6a9b0;display:flex;gap:10px}
.util-nav span.sep{color:#cfd2d7}
.main-nav{position:absolute;left:352px;top:58px;display:flex;gap:0;font-size:12px;color:#4a4d55}
.main-nav a{margin-right:28px}
.main-nav a.active{color:var(--teal)}
.nav-icons{position:absolute;left:1048px;top:54px;display:flex;gap:10px}

/* hero */
.hero{position:absolute;left:0;top:0;width:1200px;height:680px;background:linear-gradient(90deg,#e9ecf3 0%,#f3f4f8 45%,#f6f6fa 100%)}
.hero-photo{position:absolute;left:0;top:95px;width:545px;height:585px;background:linear-gradient(160deg,#e8e2dc 0%,#cfc3b8 45%,#b7a99c 100%)}
.hero-title{position:absolute;left:573px;top:232px;font-size:48px;font-weight:300;line-height:56px;color:var(--ink)}
.hero-title strong{color:var(--teal);font-weight:500}
.hero-text{position:absolute;left:576px;top:374px;width:520px;font-size:13px;line-height:24px;color:var(--muted)}
.btn{position:absolute;top:456px;height:44px;display:flex;align-items:center;justify-content:center;font-size:11px;font-weight:500;letter-spacing:.3px;text-transform:uppercase}
.btn-primary{left:575px;width:215px;background:var(--teal);color:#fff}
.btn-outline{left:805px;width:217px;border:1.5px solid var(--red);color:var(--red);background:#fff}

/* feature cards */
.feature{position:absolute;color:#fff;padding:36px 22px}
.feature h3{font-size:22px;font-weight:300;margin-bottom:22px}
.feature p{font-size:12px;line-height:22px;width:280px}
.feature .arrow{position:absolute;right:30px;bottom:16px}
.feature-teal{background:var(--teal)}
.feature-red{background:var(--red)}
.f1{left:114px;top:680px;width:316px;height:188px}
.f2{left:430px;top:663px;width:340px;height:223px;padding-top:54px;padding-left:32px}
.f3{left:770px;top:680px;width:334px;height:188px;padding-left:34px}

/* section headings */
.eyebrow{position:absolute;left:0;width:1200px;text-align:center;font-size:21px;font-weight:400;color:var(--red)}
.section-title{position:absolute;left:0;width:1200px;text-align:center;font-weight:300;color:var(--ink)}
.center-text{position:absolute;left:180px;width:840px;text-align:center;font-size:11.5px;line-height:22px;color:var(--muted)}

/* services */
.services{position:absolute;left:0;top:1312px;width:1200px;height:566px;background:linear-gradient(180deg,#dfe8ec 0%,#e7edf0 30%,#ece6dc 70%,#e6dccd 100%)}
.services-photo{position:absolute;left:500px;top:60px;width:640px;height:506px;background:radial-gradient(ellipse at 50% 60%,#e8e3dc 0%,#dcd4c9 55%,rgba(230,220,205,0) 80%)}
.services .eyebrow-left{position:absolute;left:132px;top:50px;font-size:21px;color:var(--red);font-weight:400}
.services .title-left{position:absolute;left:129px;top:80px;font-size:48px;font-weight:300;color:var(--ink)}
.service{position:absolute;left:137px;display:flex;gap:28px}
.service h4{font-size:21px;font-weight:400;margin-bottom:10px;color:var(--ink)}
.service p{font-size:11.5px;line-height:22px;color:#555960;width:230px}

/* about */
.pillar{position:absolute;top:2238px;width:330px;text-align:center}
.pillar .disc{width:86px;height:86px;border-radius:50%;margin:0 auto;display:flex;align-items:center;justify-content:center}
.pillar .disc.teal{background:var(--teal)}
.pillar .disc.red{background:var(--red)}
.pillar p{margin-top:38px;font-size:15px;font-weight:400;line-height:31px;color:var(--ink)}

/* therapists */
.therapists{position:absolute;left:0;top:2500px;width:1200px;height:566px;background:linear-gradient(90deg,#9d968c 0%,#c5b79c 30%,#d9cbb0 55%,#c8b896 100%)}
.therapists-card{position:absolute;left:544px;top:52px;width:593px;height:468px;background:#fff;padding:50px 0 0 76px}
.therapists-card .eyebrow-left{font-size:21px;color:var(--red);font-weight:400}
.therapists-card h2{font-size:48px;font-weight:300;line-height:56px;margin-top:2px;color:var(--ink)}
.issue-list{position:absolute;top:176px;list-style:none}
.issue-list li{height:38px;display:flex;align-items:center;gap:12px;font-size:11.5px;color:var(--muted);border-bottom:1px solid #f1f2f4;width:260px}
.col-a{left:76px}
.col-b{left:276px}

/* blogs */
.blog{position:absolute;top:3324px;background:var(--soft);height:367px}
.blog .thumb{width:100%;height:233px}
.blog .date{padding:26px 0 0 38px;font-size:11px;color:var(--teal)}
.blog .excerpt{padding:12px 24px 0 38px;font-size:12px;line-height:22px;color:var(--muted)}
.blog.teal{border-bottom:4px solid var(--teal)}
.blog.red{border-bottom:4px solid var(--red)}
.blog.red .date{color:var(--red)}

/* footer */
.site-footer{position:absolute;left:0;top:3790px;width:1200px;height:466px;background:var(--footer);color:#fff}
.footer-brand{position:absolute;left:150px;top:54px;display:flex;align-items:center;gap:14px}
.footer-brand .brand-dot{width:46px;height:46px}
.footer-brand .brand-name{font-size:34px;color:#fff;font-weight:400}
.footer-tag{position:absolute;left:212px;top:98px;font-size:12px;color:var(--teal)}
.social{position:absolute;left:966px;top:74px;display:flex;gap:30px}
.social span{width:18px;height:18px;border-radius:50%;background:#1f9fb0}
.footer-rule{position:absolute;left:150px;top:144px;width:972px;height:1px;background:#3a3b40}
.footer-col{position:absolute;top:200px}
.footer-col h5{font-size:21px;font-weight:400;margin-bottom:22px}
.footer-col p{font-size:11.5px;line-height:23px;color:#e2e3e6;width:380px}
.footer-col ul{list-style:none;font-size:11.5px;color:#e2e3e6}
.footer-col li{height:29px}
.contact-row{display:flex;align-items:center;gap:16px;font-size:11.5px;color:#e2e3e6;height:30px}
.copyright{position:absolute;left:167px;top:384px;font-size:11px;color:#8c8e94}
.copyright b{color:#fff;font-weight:400}
</style>
</head>
<body>

<section class="hero">
  <div class="hero-photo" role="img" aria-label="Photo of a smiling couple, woman riding piggyback on man, in soft sunlight"></div>
  <h1 class="hero-title">Expert Relationship<br>&amp; <strong>Marriage</strong> Counselling</h1>
  <p class="hero-text">We're a group of nearly 100 psychologists, counsellors and sex therapists Australia wide who are passionate about relationships.</p>
  <a class="btn btn-primary" href="#">Request an appointment</a>
  <a class="btn btn-outline" href="#">Search for therapists</a>
</section>

<header class="site-header">
  <div class="brand"><span class="brand-dot"></span><span class="brand-name">Velmora Clinic</span></div>
  <p class="brand-tag">calm support for every couple</p>
  <div class="util-nav"><a href="#">About Us</a><span class="sep">|</span><a href="#">FAQs</a><span class="sep">|</span><a href="#">Contact Us</a></div>
  <nav class="main-nav">
    <a class="active" href="#">Counsellin Types</a>
    <a href="#">Relationship Counselling Locations</a>
    <a href="#">Sex Therapy Location</a>
    <a href="#">Squizzes</a>
    <a href="#">Fees &amp; Rebates</a>
  </nav>
  <div class="nav-icons">
    <svg width="20" height="20" viewBox="0 0 20 20" fill="none" stroke="#148c98" stroke-width="1.6"><circle cx="8.5" cy="8.5" r="6"/><path d="M13 13l5 5"/></svg>
    <svg width="20" height="20" viewBox="0 0 24 24" fill="none" stroke="#148c98" stroke-width="1.6"><path d="M5 3h4l2 5-2.5 1.5a11 11 0 0 0 6 6L16 13l5 2v4a2 2 0 0 1-2 2A16 16 0 0 1 3 5a2 2 0 0 1 2-2z"/></svg>
  </div>
</header>

<article class="feature feature-teal f1">
  <h3>Relationship Counselling</h3>
  <p>We're a group of nearly 100 psychologists, counsellors and sex therapists Australia wide who are passionate</p>
  <svg class="arrow" width="14" height="10" viewBox="0 0 14 10" fill="none" stroke="#fff" stroke-width="1.5"><path d="M1 5h11M8 1l4 4-4 4"/></svg>
</article>
<article class="feature feature-red f2">
  <h3>Same Sex Relationships</h3>
  <p>We're a group of nearly 100 psychologists, counsellors and sex therapists Australia wide who are passionate</p>
  <svg class="arrow" width="14" height="10" viewBox="0 0 14 10" fill="none" stroke="#fff" stroke-width="1.5"><path d="M1 5h11M8 1l4 4-4 4"/></svg>
</article>
<article class="feature feature-teal f3">
  <h3>Sexual Issues Counselling</h3>
  <p>We're a group of nearly 100 psychologists, counsellors and sex therapists Australia wide who are passionate</p>
  <svg class="arrow" width="14" height="10" viewBox="0 0 14 10" fill="none" stroke="#fff" stroke-width="1.5"><path d="M1 5h11M8 1l4 4-4 4"/></svg>
</article>

<section class="specialise">
  <p class="eyebrow" style="top:976px">We Specialise in</p>
  <h2 class="section-title" style="top:1010px;font-size:31px">We Specialise in Relationship &amp; Marriage Counselling</h2>
  <p class="center-text" style="top:1073px">You've come to the right place if you value your relationship, (along with being true to yourself) and would like help with how to repair the inevitable difficulties that come up in most relationships, and build a stronger more authentic connection.</p>
  <p class="center-text" style="top:1139px">None of us, when we fall in love, imagine how difficult our relationship is going to be at times. We always hope for the best, then do our best, and still we can find that we can get stranded in problems that we don't really understand. We can unwittingly get into distressing lose-lose negative cycles, and not know how to get out of them.</p>
</section>

<section class="services">
  <div class="services-photo" role="img" aria-label="Photo of a couple in hats sitting on a beach with arms raised toward the sea"></div>
  <p class="eyebrow-left">What We Offer</p>
  <h2 class="title-left">Our Services</h2>
  <div class="service" style="top:168px">
    <svg width="58" height="58" viewBox="0 0 58 58" fill="none" stroke="#2b2d33" stroke-width="2"><circle cx="21" cy="36" r="14"/><circle cx="37" cy="36" r="14"/><path d="M21 22l-5-8h10z"/></svg>
    <div><h4>Relationship Counselling</h4><p>Communication, recovering from an affair, loss of intimacy and love or</p></div>
  </div>
  <div class="service" style="top:298px">
    <svg width="58" height="58" viewBox="0 0 58 58" fill="none" stroke="#2b2d33" stroke-width="2"><circle cx="18" cy="22" r="8"/><circle cx="40" cy="22" r="8"/><path d="M4 52v-8a10 10 0 0 1 10-10h8a10 10 0 0 1 10 10v8M26 52v-8a10 10 0 0 1 10-10h8a10 10 0 0 1 10 10v8M2 53h54"/></svg>
    <div><h4>Sex Therapy Counselling</h4><p>Low sexual drive, erectile difficulties, premature ejaculation,</p></div>
  </div>
  <div class="service" style="top:424px">
    <svg width="58" height="58" viewBox="0 0 58 58" fill="none" stroke="#2b2d33" stroke-width="2"><path d="M10 40l14-24 6 4-6 14 12-16 6 4-10 16 10-8 4 5-16 16H18z"/></svg>
    <div><h4>Anger Management</h4><p>Managing irrational outbursts, while learning to express your anger in</p></div>
  </div>
</section>

<section class="about">
  <p class="eyebrow" style="top:1966px">Who We Are</p>
  <h2 class="section-title" style="top:1992px;font-size:48px">About Velmora Clinic</h2>
  <p class="center-text" style="top:2080px;left:215px;width:770px">Our vision is to be the most highly regarded and comprehensive marriage counselling, relationship counselling and sex therapy service in Australia, at reasonable and affordable rates.</p>
  <p class="center-text" style="top:2146px;left:215px;width:770px">We hand choose our team of Registered Psychologists, Counsellors and Sex Therapists considering their knowledge, compassion, and unbiased approach to marriage counselling and sexual therapy and their experience in the relationship field.</p>
  <div class="pillar" style="left:152px">
    <div class="disc teal"><svg width="40" height="40" viewBox="0 0 40 40" fill="none" stroke="#fff" stroke-width="2"><rect x="9" y="6" width="22" height="28" rx="6"/><path d="M14 30h12M15 18h10"/></svg></div>
    <p>Our Marriage Counselling<br>Approach</p>
  </div>
  <div class="pillar" style="left:437px">
    <div class="disc red"><svg width="40" height="40" viewBox="0 0 40 40" fill="none" stroke="#fff" stroke-width="2"><path d="M20 30s-11-7-11-14a6 6 0 0 1 11-3 6 6 0 0 1 11 3c0 7-11 14-11 14z"/></svg></div>
    <p>Our Marriage Counselling<br>Locations</p>
  </div>
  <div class="pillar" style="left:733px">
    <div class="disc teal"><svg width="40" height="40" viewBox="0 0 40 40" fill="none" stroke="#fff" stroke-width="2"><circle cx="15" cy="24" r="8"/><circle cx="25" cy="20" r="8"/><path d="M30 15l5-5M30 10h5v5"/></svg></div>
    <p>Communication is a vital skill but not<br>often taught to us</p>
  </div>
</section>

<section class="therapists">
  <div class="abs" style="left:0;top:0;width:544px;height:566px" role="img" aria-label="Photo of a couple embracing in a field of tall golden grass"></div>
  <div class="therapists-card">
    <p class="eyebrow-left">Our Relationship</p>
    <h2>Therapists</h2>
    <ul class="issue-list col-a">
      <li><svg width="14" height="14" viewBox="0 0 14 14" fill="none" stroke="#148c98" stroke-width="1.4"><circle cx="7" cy="7" r="6"/><path d="M4 7l2 2 4-4"/></svg>Affairs</li>
      <li><svg width="14" height="14" viewBox="0 0 14 14" fill="none" stroke="#148c98" stroke-width="1.4"><circle cx="7" cy="7" r="6"/><path d="M4 7l2 2 4-4"/></svg>Controlling behaviour</li>
      <li><svg width="14" height="14" viewBox="0 0 14 14" fill="none" stroke="#148c98" stroke-width="1.4"><circle cx="7" cy="7" r="6"/><path d="M4 7l2 2 4-4"/></svg>Verbal abuse</li>
      <li><svg width="14" height="14" viewBox="0 0 14 14" fill="none" stroke="#148c98" stroke-width="1.4"><circle cx="7" cy="7" r="6"/><path d="M4 7l2 2 4-4"/></svg>Imbalance of power</li>
      <li><svg width="14" height="14" viewBox="0 0 14 14" fill="none" stroke="#148c98" stroke-width="1.4"><circle cx="7" cy="7" r="6"/><path d="M4 7l2 2 4-4"/></svg>Lack of intimacy</li>
      <li><svg width="14" height="14" viewBox="0 0 14 14" fill="none" stroke="#148c98" stroke-width="1.4"><circle cx="7" cy="7" r="6"/><path d="M4 7l2 2 4-4"/></svg>Poor communication</li>
      <li><svg width="14" height="14" viewBox="0 0 14 14" fill="none" stroke="#148c98" stroke-width="1.4"><circle cx="7" cy="7" r="6"/><path d="M4 7l2 2 4-4"/></svg>Loss of love</li>
    </ul>
    <ul class="issue-list col-b">
      <li><svg width="14" height="14" viewBox="0 0 14 14" fill="none" stroke="#148c98" stroke-width="1.4"><circle cx="7" cy="7" r="6"/><path d="M4 7l2 2 4-4"/></svg>Relationship neglect</li>
      <li><svg width="14" height="14" viewBox="0 0 14 14" fill="none" stroke="#148c98" stroke-width="1.4"><circle cx="7" cy="7" r="6"/><path d="M4 7l2 2 4-4"/></svg>Sexual problems</li>
      <li><svg width="14" height="14" viewBox="0 0 14 14" fill="none" stroke="#148c98" stroke-width="1.4"><circle cx="7" cy="7" r="6"/><path d="M4 7l2 2 4-4"/></svg>Problems from childhood</li>
      <li><svg width="14" height="14" viewBox="0 0 14 14" fill="none" stroke="#148c98" stroke-width="1.4"><circle cx="7" cy="7" r="6"/><path d="M4 7l2 2 4-4"/></svg>Problems with parenting your children</li>
      <li><svg width="14" height="14" viewBox="0 0 14 14" fill="none" stroke="#148c98" stroke-width="1.4"><circle cx="7" cy="7" r="6"/><path d="M4 7l2 2 4-4"/></svg>Step children and in-laws</li>
      <li><svg width="14" height="14" viewBox="0 0 14 14" fill="none" stroke="#148c98" stroke-width="1.4"><circle cx="7" cy="7" r="6"/><path d="M4 7l2 2 4-4"/></svg>All forms of family problems</li>
      <li><svg width="14" height="14" viewBox="0 0 14 14" fill="none" stroke="#148c98" stroke-width="1.4"><circle cx="7" cy="7" r="6"/><path d="M4 7l2 2 4-4"/></svg>Anger management problems</li>
    </ul>
  </div>
</section>

<section class="blogs">
  <h2 class="section-title" style="top:3142px;font-size:48px">Latest Blogs</h2>
  <p class="center-text" style="top:3224px;left:370px;width:460px">Our vision is to be the most highly regarded and comprehensive marriage counselling, relationship counselling</p>
  <article class="blog teal" style="left:114px;width:321px">
    <div class="thumb" role="img" aria-label="Photo of hands holding a wedding ring" style="background:linear-gradient(135deg,#e8e6e4,#b9b2ad)"></div>
    <p class="date">24 June 2020</p>
    <p class="excerpt">What is Borderline Personality Disorder and how does it affect my relationship?</p>
  </article>
  <article class="blog red" style="left:450px;width:319px">
    <div class="thumb" role="img" aria-label="Photo of a smiling mature couple" style="background:linear-gradient(135deg,#c9cfd6,#9fb2c6)"></div>
    <p class="date">05 May 2020</p>
    <p class="excerpt">Sexual Desires in Men and Women; What Are the Real Differences?</p>
  </article>
  <article class="blog teal" style="left:784px;width:320px">
    <div class="thumb" role="img" aria-label="Photo of a couple lying close together on green grass" style="background:linear-gradient(135deg,#8fbf62,#4f8a34)"></div>
    <p class="date">24 June 2020</p>
    <p class="excerpt">What is Borderline Personality Disorder and how does it affect my relationship?</p>
  </article>
</section>

<footer class="site-footer">
  <div class="footer-brand"><span class="brand-dot"></span><span class="brand-name">Velmora Clinic</span></div>
  <p class="footer-tag">calm support for every couple</p>
  <div class="social" aria-label="Social links"><span></span><span></span><span></span><span></span></div>
  <div class="footer-rule"></div>
  <div class="footer-col" style="left:167px">
    <h5>About Us</h5>
    <p>Our vision is to be the most highly regarded and comprehensive marriage counselling, relationship counselling and sex therapy service in Australia, at reasonable and affordable rates.</p>
  </div>
  <div class="footer-col" style="left:688px">
    <h5>Links</h5>
    <ul><li>Home</li><li>About Us</li><li>Our Blogs</li><li>Members Log In</li><li>Contact Us</li></ul>
  </div>
  <div class="footer-col" style="left:929px">
    <h5>Contact Us</h5>
    <div class="contact-row"><svg width="16" height="16" viewBox="0 0 24 24" fill="#1f9fb0"><path d="M5 3h4l2 5-2.5 1.5a11 11 0 0 0 6 6L16 13l5 2v4a2 2 0 0 1-2 2A16 16 0 0 1 3 5a2 2 0 0 1 2-2z"/></svg>1300 555 014</div>
    <div class="contact-row"><svg width="16" height="12" viewBox="0 0 16 12" fill="none" stroke="#1f9fb0" stroke-width="1.5"><rect x="1" y="1" width="14" height="10"/><path d="M1 1l7 6 7-6"/></svg>info@velmoraclinic.com.au</div>
  </div>
  <p class="copyright">© 2020 <b>Velmora Clinic.</b> All rights reserved.</p>
</footer>

</body>
</html>
```